Clean book cover design for book about writing a book

Book title: The Crossing
Subtitle: 9 Paths to Crafting a Volume that Counts
Name: Marisol T. Brenwick, The Quill Nursery

This is a book which teaches 10 steps to writing a self-help book. I'm looking for a very clean impactful cover either with no image or just a small simple image of a book, typewriter, laptop, cabin or something very simple. I am attaching the manuscript here if reading it would help you with the cover. The theme of the book is that you can write with joy and ease and your book can just flow out of you if you learn how to clear the blocks between you and your book already written. Sort of a new agey stance on book writing.

The book should generally match the branding on my website. Www.TheQuillNursery.example.

I have photos of myself attached which I'd like used for the back cover with an "about the author section of maybe 50 words.

The project is for the full back cover and spine as well as the front cover (see print Forge template attached) but to win the contest you can just design the front cover and then I'll give the winner the template for the full design with the back cover copy. Or you can design the full cover using the template and you can use Loren ipsum text if you need to.

My clients are very upmarket and the themes of my business revolve around nuturing and incubating ideas and authors. Very feminine creation energy.

For colors see The Crossing Press (CB) wax seals and the background fades. I don't want my logo on the cover but I am attaching it here so you get a feel for the branding. The logo is in the LOBSTER font and you can see how we do the grey with the rainbow shadow.

Here are some covers I like:

http://www.shopvale.example/Pen-Tome-Quick-Stage---Stage/dp/055817342Q
http://www.shopvale.example/Plotting-Your-Tale-Chart-Triumph/dp/0841739265
http://www.shopvale.example/Be-Scribe-Seeking-Voice-Guide-ebook/dp/K22R9WQ3L1
http://www.shopvale.example/Strays-Tale-Triumph-Rupert-Vanhollow/dp/0552048871
Updates

I have revised my brief to include some picture and images that will help you create the cover. I have also included some of my favorite covers to give you more of a sense of what I'm going for. And I have included the manuscript in case it would help you to skim through it in order to get a sense of the reader and the book. I think if you look at my revised brief it will make it easier to create a submission. Thanks!

Target Market(s)

Women 40-60 who run small businesses as life coaches or other healing jobs (therapy, reiki, light work) they have a spiritual/new age bent.

Industry/Entity Type

Business

Font styles to use
Serif
Other font styles liked:
• Lobster (not required... just a suggestion since it's my logo font)

Requirements
Must have
• Name and title easy to read in 1" x 1" thumb nail
Nice to have
• Fantastic type face treatment.

Match the look and feel of my website.
Should not have
• Busy images. With one simple image or just designed with colors and typeface treatment

```html
<!DOCTYPE html>
<html lang="en">
<head>
<meta charset="utf-8">
<title>The Crossing — Cover Options</title>
<link rel="stylesheet" href="https://fonts.googleapis.com/css2?family=Lobster&family=Courier+Prime:wght@400;700&family=Josefin+Sans:wght@600;700&display=swap">
<style>
  :root {
    --page: #ffffff;
    --ink: #141414;
    --ink-soft: #2a2a2a;
    --paper-light: #fbfbfb;
    --paper-mid: #e9e9e9;
    --paper-edge: #cfcfcf;
    --pages-light: #f3d9a8;
    --pages-deep: #c98e3f;
    --pages-shadow: #6b5a44;
    --teal: #2f9b87;
    --teal-deep: #1f7467;
    --orange: #f27a18;
    --orange-deep: #c85a08;
    --brand-grey: #8a8a8a;
  }
  * { box-sizing: border-box; margin: 0; padding: 0; }
  html, body {
    width: 1200px; height: 968px; overflow: hidden;
    background: var(--page);
  }
  .cover-sheet {
    position: relative; width: 1200px; height: 968px;
    display: flex; justify-content: space-between;
    padding: 10px;
  }
  .cover {
    position: relative; width: 578px; height: 948px; overflow: hidden;
    background:
      linear-gradient(135deg, rgba(255,255,255,0) 40%, rgba(0,0,0,0.035) 40.2%, rgba(0,0,0,0) 62%),
      linear-gradient(60deg, rgba(0,0,0,0.03) 0 30%, rgba(255,255,255,0) 30.2%),
      linear-gradient(300deg, rgba(0,0,0,0.04) 0 22%, rgba(255,255,255,0) 22.2%),
      radial-gradient(ellipse at 50% 45%, var(--paper-light) 0%, var(--paper-mid) 60%, var(--paper-edge) 100%);
  }
  .cover--teal { --accent: var(--teal); --accent-deep: var(--teal-deep); }
  .cover--orange { --accent: var(--orange); --accent-deep: var(--orange-deep); }

  .title {
    position: absolute; left: 0; right: 0; top: 18px;
    font-family: "Lobster", cursive; font-weight: 400;
    color: var(--ink); text-align: center; line-height: 1;
  }
  .title__lead {
    display: block; font-size: 84px;
    padding-left: 200px; letter-spacing: 1px;
  }
  .title__main {
    display: block; font-size: 168px; margin-top: -28px;
    letter-spacing: -1px;
  }
  .title__accent {
    color: var(--accent);
    text-shadow: 2px 3px 0 var(--accent-deep);
  }

  .subtitle {
    position: absolute; left: 0; right: 0; top: 264px;
    font-family: "Courier Prime", monospace; color: var(--ink);
    text-align: center; text-transform: uppercase;
  }
  .subtitle__count { display: block; font-size: 34px; letter-spacing: 3px; }
  .subtitle__rest { display: block; font-size: 20px; letter-spacing: 1px; margin-top: 6px; }

  .book-art {
    position: absolute; left: 50px; top: 360px; width: 500px; height: 400px;
  }

  .author {
    position: absolute; left: 0; right: 0; top: 800px;
    font-family: "Josefin Sans", sans-serif; font-weight: 700;
    font-size: 34px; letter-spacing: 8px; text-transform: uppercase;
    color: var(--ink-soft); text-align: center;
  }
  .imprint {
    position: absolute; left: 0; right: 0; top: 866px;
    font-family: "Josefin Sans", sans-serif; font-weight: 600;
    font-size: 22px; letter-spacing: 2px; color: var(--brand-grey);
    text-align: center; text-transform: uppercase;
  }
</style>
</head>
<body>
<main class="cover-sheet">
  <article class="cover cover--teal">
    <h1 class="title">
      <span class="title__lead">The</span>
      <span class="title__main">Cro<span class="title__accent">ss</span>ing</span>
    </h1>
    <p class="subtitle">
      <span class="subtitle__count">9 Paths</span>
      <span class="subtitle__rest">to crafting a volume that counts</span>
    </p>
    <svg class="book-art" viewBox="0 0 500 400" role="img" aria-label="Illustration of an open book with pages fanning upward">
      <defs>
        <radialGradient id="pagesTeal" cx="50%" cy="55%" r="60%">
          <stop offset="0%" stop-color="#f3d9a8"/>
          <stop offset="70%" stop-color="#c98e3f"/>
          <stop offset="100%" stop-color="#c98e3f" stop-opacity="0"/>
        </radialGradient>
        <radialGradient id="shadowTeal" cx="50%" cy="50%" r="50%">
          <stop offset="0%" stop-color="#6b5a44" stop-opacity="0.55"/>
          <stop offset="100%" stop-color="#6b5a44" stop-opacity="0"/>
        </radialGradient>
      </defs>
      <ellipse cx="220" cy="350" rx="190" ry="40" fill="url(#shadowTeal)"/>
      <ellipse cx="250" cy="220" rx="250" ry="170" fill="url(#pagesTeal)"/>
    </svg>
    <p class="author">Marisol T. Brenwick</p>
    <p class="imprint">The Quill Nursery</p>
  </article>

  <article class="cover cover--orange">
    <h1 class="title">
      <span class="title__lead">The</span>
      <span class="title__main">Cro<span class="title__accent">ss</span>ing</span>
    </h1>
    <p class="subtitle">
      <span class="subtitle__count">9 Paths</span>
      <span class="subtitle__rest">to crafting a volume that counts</span>
    </p>
    <svg class="book-art" viewBox="0 0 500 400" role="img" aria-label="Illustration of an open book with pages fanning upward">
      <defs>
        <radialGradient id="pagesOrange" cx="50%" cy="55%" r="60%">
          <stop offset="0%" stop-color="#f3d9a8"/>
          <stop offset="70%" stop-color="#c98e3f"/>
          <stop offset="100%" stop-color="#c98e3f" stop-opacity="0"/>
        </radialGradient>
        <radialGradient id="shadowOrange" cx="50%" cy="50%" r="50%">
          <stop offset="0%" stop-color="#6b5a44" stop-opacity="0.55"/>
          <stop offset="100%" stop-color="#6b5a44" stop-opacity="0"/>
        </radialGradient>
      </defs>
      <ellipse cx="220" cy="350" rx="190" ry="40" fill="url(#shadowOrange)"/>
      <ellipse cx="250" cy="220" rx="250" ry="170" fill="url(#pagesOrange)"/>
    </svg>
    <p class="author">Marisol T. Brenwick</p>
    <p class="imprint">The Quill Nursery</p>
  </article>
</main>
</body>
</html>
```